Signwriting for Halvorn Tradeline Van

I've bought a Halvorn Tradeline van for my business, and want to signwrite the sides and back. Can you help me come up with a very eyecatching design? I hope so!
Brief:
Design eye-catching signwriting for the sides and rear of a Halvorn Tradeline van that will raise brand recognition for our business.
The Business:
The business is called Brightbox Supply. We basically sell glass display cabinets and display cases. These are mostly used for commercial purposes (mainly retail), but also for residential. You can see what we sell on our website: www.brightboxsupply.co.nz.
The business is located in Auckland, New Zealand.
The Van:
The van is a 2009 Halvron Tradeline, super high roof and medium wheel base. It is painted silver, so consider silver the base colour.
The van has no rear windows, so the signwriting needn't avoid any windows.
The van will be used for deliveries and other general purposes for the business, and while it is out and about I'd like it to be identifiable for where it is from and what it is doing.
The whole van is 2.6 metres tall, 1.9 metres wide and 5.75 metres long.
The Creative Brief:
The signwriting MUST:
- be very eye-catching. I don't just want a magnet on the side of the van. It must stand out from the crowd.
- be recognisable as representative of a business selling glass display cases.
- use the business logo on both sides.
- include the web address.
- consider cost as a factor in the design. I understand that great signwriting will cost money, but cost is also a factor.
The signwriting MAY:
- use other images, although it does not necessarily need to.
- use other colours beside the corporate colours of green, grey, purple and black. Remember that the van is painted silver. The CMYK colours are available upon request.
- cover the whole van, or it may cover part of it.
- be a partial or ful vehicle wrap, or it may be a vinyl print that is adhered to the van.
Glass is one of the hardest materials to represent visually. This leads me to think that an abstract design may work better, but the right photographic image could be used.
The attachments:
1. Company logo
2. A file showing some vehicle signwriting I really like. I am NOT asking you to do exactly the same thing, but I'm showing you what I think eye-catching vehicle graphics look like.
3. Photos of the van.

```html
<!DOCTYPE html>
<html lang="en">
<head>
<meta charset="utf-8">
<title>Brightbox Supply – Rear Van Signwriting</title>
<link rel="stylesheet" href="https://fonts.googleapis.com/css2?family=Jost:wght@300;400;600;700&display=swap">
<style>
  :root {
    --backdrop: #f4f4f4;
    --wrap-green: #a6d66f;
    --wrap-green-deep: #95c95c;
    --ink-white: #ffffff;
    --accent-orange: #f07a1c;
    --accent-dark: #3a3a3a;
    --seam: rgba(80, 120, 40, 0.35);
  }
  * { margin: 0; padding: 0; box-sizing: border-box; }
  html, body {
    width: 1200px;
    height: 600px;
    overflow: hidden;
    background: var(--backdrop);
    font-family: "Jost", "Helvetica Neue", Arial, sans-serif;
  }
  .canvas {
    position: relative;
    width: 1200px;
    height: 600px;
  }
  .rear-panel {
    position: absolute;
    left: 395px;
    top: 36px;
    width: 410px;
    height: 500px;
    background: linear-gradient(180deg, var(--wrap-green) 0%, var(--wrap-green-deep) 100%);
    border-radius: 34px 34px 10px 10px;
    overflow: hidden;
  }
  .door-seam {
    position: absolute;
    left: 204px;
    top: 0;
    width: 1px;
    height: 100%;
    background: var(--seam);
  }
  .headline {
    position: absolute;
    top: 34px;
    left: 0;
    width: 100%;
    text-align: center;
    color: var(--ink-white);
    font-weight: 300;
    font-size: 19.5px;
    line-height: 25px;
    letter-spacing: 0.3px;
    text-transform: uppercase;
  }
  .headline strong {
    font-weight: 700;
    font-size: 21px;
  }
  .pattern-strip {
    position: absolute;
    left: 173px;
    top: 200px;
    width: 64px;
    height: 300px;
    background: linear-gradient(180deg, rgba(255,255,255,0.55) 0%, rgba(255,255,255,0.3) 50%, rgba(255,255,255,0.55) 100%);
  }
  .contact-bars {
    position: absolute;
    left: 260px;
    top: 372px;
    width: 150px;
  }
  .contact-bar {
    position: relative;
    height: 15px;
    margin-bottom: 4px;
    background: var(--accent-orange);
    color: var(--ink-white);
    font-size: 7.5px;
    line-height: 15px;
    text-align: right;
    padding-right: 10px;
    white-space: nowrap;
  }
  .contact-bar b { font-weight: 600; }
  .contact-bar::before {
    content: "";
    position: absolute;
    top: 0;
    left: -14px;
    width: 22px;
    height: 15px;
    background: var(--accent-dark);
    transform: skewX(-40deg);
  }
  .contact-bar.phone { margin-left: 24px; }
  .contact-bar.fax { margin-left: 12px; }
  .contact-bar.email { margin-left: 0; }
  .brand {
    position: absolute;
    left: 244px;
    top: 440px;
    color: var(--ink-white);
  }
  .brand-line {
    display: flex;
    align-items: center;
    gap: 6px;
  }
  .brand-mark {
    width: 12px;
    height: 12px;
    background: var(--ink-white);
  }
  .brand-name {
    font-size: 14px;
    font-weight: 400;
    text-transform: uppercase;
    letter-spacing: 0.2px;
  }
  .brand-tagline {
    margin-left: 18px;
    font-size: 8.5px;
    font-weight: 300;
    line-height: 10px;
  }
</style>
</head>
<body>
  <main class="canvas">
    <section class="rear-panel" aria-label="Rear door signwriting">
      <div class="door-seam"></div>

      <h1 class="headline">
        Suppliers of<br>
        <strong>High Quality</strong><br>
        Showcases,<br>
        Display Cases<br>
        and<br>
        Display Cabinets
      </h1>

      <div class="pattern-strip" role="img" aria-label="Vertical band of stacked translucent diamond shapes down the door seam"></div>

      <div class="contact-bars">
        <p class="contact-bar phone">Phone <b>027 418 5206</b></p>
        <p class="contact-bar fax">Fax <b>(09) 357 2814</b></p>
        <p class="contact-bar email">Email <b>info@brightboxsupply.co.nz</b></p>
      </div>

      <div class="brand">
        <div class="brand-line">
          <span class="brand-mark"></span>
          <span class="brand-name">Brightbox Supply</span>
        </div>
        <p class="brand-tagline">design strength value</p>
      </div>
    </section>
  </main>
</body>
</html>
```